Tin Lantern

I have written a book which I eventually would like to serve a couple of purposes. The initial purpose was to memorialize life events and lessons from my life to pass on to my grandchildren, in hopes they may learn from the experiences. As I completed the book, I now believe I could remove some of the family specific information as much of the information could be useful to many people.

While I want to book to have a great look for the grandkids, more importantly will be the version that we put on the bookshelf to sell. The cover is obviously the first thing a buyer will see and may or may not peak there interest. I would like to include the attached photo as the cover photo and the title language is also attached. Other than that I am not sure what is the best way to design the cover.

```html
<!DOCTYPE html>
<html lang="en">
<head>
<meta charset="utf-8">
<title>It's Called Life — Grandpa Halvorsen</title>
<link rel="stylesheet" href="https://fonts.googleapis.com/css2?family=Arimo:ital,wght@0,400;0,700;1,700&display=swap">
<style>
  :root {
    --backdrop: #1c1c1c;
    --cover-red: #be1e2d;
    --panel-light: #f6f6f7;
    --panel-mid: #e4e5e7;
    --ink: #111111;
    --white: #ffffff;
    --photo-dark: #3a2a20;
    --photo-mid: #7a5b45;
    --photo-light: #b59a82;
  }
  * { margin: 0; padding: 0; box-sizing: border-box; }
  html, body {
    width: 1200px; height: 900px; overflow: hidden;
    background: var(--backdrop);
    font-family: "Arimo", Arial, sans-serif;
    color: var(--ink);
  }
  .stage { position: relative; width: 1200px; height: 900px; }
  .book-cover {
    position: absolute; left: 345px; top: 62px;
    width: 511px; height: 777px;
    background: var(--cover-red);
  }
  .cover-panel {
    position: absolute; left: 12px; top: 12px;
    width: 487px; height: 676px;
    background: radial-gradient(ellipse at 50% 45%, var(--panel-light) 0%, var(--panel-mid) 100%);
  }
  .greeting {
    position: absolute; left: 0; right: 0; top: 30px;
    text-align: center; font-weight: 700; font-size: 43px; letter-spacing: 0.5px;
  }
  .cover-photo {
    position: absolute; left: 19px; top: 96px;
    width: 449px; height: 284px;
    border: 3px solid var(--cover-red);
    background: linear-gradient(160deg, var(--photo-dark) 0%, var(--photo-mid) 45%, var(--photo-light) 75%, var(--photo-mid) 100%);
    box-shadow: 0 3px 6px rgba(0,0,0,0.25);
  }
  .grandchildren {
    position: absolute; left: 0; right: 0; top: 393px;
    text-align: center; font-weight: 700; font-size: 15px; line-height: 19px;
  }
  .tagline {
    position: absolute; left: 70px; top: 453px;
    font-weight: 700; font-style: italic; font-size: 20px; letter-spacing: 0.3px;
  }
  .title-block { position: absolute; right: 27px; top: 506px; text-align: right; }
  .title-lead {
    display: inline-block; font-weight: 700; font-size: 28px;
    vertical-align: baseline; margin-right: 4px;
  }
  .title-word {
    display: inline-block; font-weight: 700; font-size: 120px; line-height: 96px;
    color: var(--cover-red); letter-spacing: -4px; vertical-align: baseline;
    transform: scaleX(0.92); transform-origin: right bottom;
  }
  .title-aside {
    position: absolute; right: 27px; top: 613px;
    font-weight: 700; font-size: 15px;
  }
  .closing-line {
    position: absolute; left: 0; right: 0; top: 646px;
    text-align: center; font-weight: 700; font-style: italic; font-size: 23px; letter-spacing: 1.2px;
  }
  .author-band {
    position: absolute; left: 0; right: 0; bottom: 0; height: 89px;
    display: flex; align-items: center; justify-content: center;
    color: var(--white); font-weight: 700; font-size: 28px;
    padding-bottom: 8px;
  }
</style>
</head>
<body>
<main class="stage">
  <article class="book-cover">
    <section class="cover-panel">
      <h1 class="greeting">Hi Guys……………</h1>
      <div class="cover-photo" role="img" aria-label="Family photograph: a grandfather seated on a porch step surrounded by his seven grandsons"></div>
      <p class="grandchildren">Owen &nbsp;|&nbsp; Gabriel &nbsp;|&nbsp; Beau &nbsp;|&nbsp; Luke<br>Elliot &nbsp;|&nbsp; Simon &nbsp;|&nbsp; Theodore</p>
      <p class="tagline">There’s a bump in the road ahead……</p>
      <h2 class="title-block"><span class="title-lead">It’s called</span><span class="title-word">LIFE</span></h2>
      <p class="title-aside">(and life isn’t fair)</p>
      <p class="closing-line">This is about having a great one.</p>
    </section>
    <footer class="author-band">Grandpa Halvorsen</footer>
  </article>
</main>
</body>
</html>
```